Specialized tax accounting firm needs marketing postcard

We need a postcard design for a professional services firm called R. Winslow Farrow Inc. The firm is essentially a very specialized tax accounting firm - instead of serving the end consumer, we support other public accounting firms in the area of Canadian and U.S. tax advisory and compliance (i.e. they call us on tax issues too complex for the general practitioner). Our byline is "Tax Support Services for Public Accounting Firms". Our postcard should utilize our logo and be based on colours present in our logo (see file attached). The final design needs to convey professionalism and trustworthiness (we're hired by accountants after all!) while being creative and eye-catching. Eye-catching is critical, since many prospective recipients will not have heard from me before and I want them to read the postcard.

I've attached:
The font used in the logo
The logo itself in a variety of file formats
A picture of myself for incorporation in the postcard
A sample postcard from Publisher showing the wording to be used in the postcard and the elements to be included

Please note that in including a draft postcard I don't want the designer to follow the layout as is. It just shows the basic elements I want included. The only element which should remain constant is the wording - I do want the text elements included as written - however, everything else - font, size, placement of elements, etc. is up for creative ideas.

Please note that there is much more leather background around the logo than needs to be incorporated in the letterhead.

Industry/Entity Type

Accounting

```html
<!DOCTYPE html>
<html lang="en">
<head>
<meta charset="utf-8">
<title>R. Winslow Farrow Inc. – Postcard</title>
<link rel="stylesheet" href="https://fonts.googleapis.com/css2?family=Roboto+Condensed:wght@400;700&display=swap">
<style>
  :root{
    --page:#ecebe8;
    --ink:#1c1c1c;
    --frame:#161616;
    --panel:#2b2a2a;
    --paper:#ffffff;
    --text-dark:#2a2a2a;
    --text-light:#f1f1f1;
    --gold:#f2c01e;
    --blue:#2b63a8;
    --rule:#8c8c8c;
  }
  *{box-sizing:border-box;margin:0;padding:0}
  html,body{width:1200px;height:800px;overflow:hidden}
  body{
    background:var(--page);
    font-family:"Roboto Condensed","Arial Narrow",sans-serif;
    position:relative;
  }
  .postcard{
    position:absolute;top:190px;width:560px;height:420px;
    box-shadow:0 6px 18px rgba(0,0,0,.18);
    overflow:hidden;
  }
  /* ---------- front ---------- */
  .postcard--front{left:25px;background:var(--frame);padding:16px}
  .front-inner{position:relative;width:100%;height:100%;background:var(--paper);overflow:hidden}
  .front-visual{
    position:absolute;top:0;right:0;width:64%;height:78%;
    background:
      linear-gradient(to right,#fff 0%,rgba(255,255,255,0) 38%),
      linear-gradient(to top,#fff 0%,rgba(255,255,255,0) 35%),
      linear-gradient(150deg,#e8c6cb 0%,#b9394a 18%,#f3eeee 30%,#2d3c6e 42%,#5b6488 52%,#c8cbd2 66%,#8f939a 82%,#e2e3e6 100%);
  }
  .brand-bar{
    position:absolute;top:96px;left:18px;width:262px;height:56px;
    background:var(--frame);display:flex;align-items:center;gap:10px;padding:0 12px;
  }
  .brand-mark{width:20px;height:20px;background:var(--blue);flex:none}
  .brand-name{color:#fff;font-weight:400;font-size:19px;letter-spacing:1.5px;text-transform:uppercase;line-height:1}
  .brand-tagline{color:#d8d8d8;font-size:6.5px;letter-spacing:.9px;text-transform:uppercase;margin-top:4px}
  .front-copy{position:absolute;top:166px;left:18px;width:330px;color:var(--text-dark)}
  .front-heading{font-size:19px;font-weight:400;text-transform:uppercase;line-height:1.05;letter-spacing:.2px;margin-bottom:8px}
  .front-copy p{font-size:11px;line-height:1.3;text-align:justify;margin-bottom:9px}

  /* ---------- back ---------- */
  .postcard--back{right:25px;background:var(--paper);border:1px solid #d6d6d6}
  .back-panel{
    position:absolute;top:0;left:0;width:286px;height:100%;
    background:var(--panel);color:var(--text-light);padding:36px 18px 0 16px;
  }
  .back-brand{display:flex;align-items:center;gap:8px;margin-bottom:26px}
  .back-brand .brand-mark{width:18px;height:18px}
  .back-brand .brand-name{font-size:16px}
  .back-brand .brand-tagline{font-size:5.5px}
  .back-panel p{font-size:11px;line-height:1.3;margin-bottom:10px}
  .contact{position:absolute;left:16px;top:282px;font-size:11px;line-height:1.35}
  .contact-name{margin-bottom:8px}
  .contact-row{display:flex;align-items:flex-start;gap:6px;margin-bottom:3px}
  .contact-row svg{flex:none;margin-top:2px}
  .portrait{
    position:absolute;left:192px;top:284px;width:72px;height:108px;
    background:linear-gradient(180deg,#8a8f96 0%,#6f6a66 45%,#3a3a3e 100%);
    border:2px solid #555;
  }
  .stamp-box{
    position:absolute;top:38px;right:36px;width:62px;height:62px;border:1px solid #444;
    font-size:8px;display:flex;align-items:center;justify-content:center;color:#222;
  }
  .address-line{position:absolute;left:304px;width:222px;height:1px;background:var(--rule)}
</style>
</head>
<body>

<section class="postcard postcard--front" aria-label="Postcard front">
  <div class="front-inner">
    <div class="front-visual" role="img" aria-label="Photo of a U.S. flag, calculator and pen resting on a tax form"></div>
    <div class="brand-bar">
      <span class="brand-mark"></span>
      <div>
        <div class="brand-name">R. Winslow Farrow Inc.</div>
        <div class="brand-tagline">Tax Support Services for Public Accounting Firms</div>
      </div>
    </div>
    <div class="front-copy">
      <h1 class="front-heading">Do your clients need help<br>with their U.S. taxes?</h1>
      <p>You probably know that U.S. citizens have to file U.S. tax returns every year—even if they live in Canada. So do your clients. That’s why they’re asking you if you know anyone who can help them with their U.S. filings.</p>
      <p>Finding a tax accountant who can help with U.S. filings is tough. U.S. tax preparers have to be registered with the IRS to be eligible to prepare U.S. returns. Your client needs someone with experience, someone timely, someone charging a reasonable price. With a proven track record of over 15 years, I can deliver.</p>
      <p>Feel free to pass along my contact information to your clients. I’d be glad to chat.</p>
    </div>
  </div>
</section>

<section class="postcard postcard--back" aria-label="Postcard back">
  <div class="back-panel">
    <div class="back-brand">
      <span class="brand-mark"></span>
      <div>
        <div class="brand-name">R. Winslow Farrow Inc.</div>
        <div class="brand-tagline">Tax Support Services for Public Accounting Firms</div>
      </div>
    </div>
    <p>R. Winslow Farrow Inc. is a boutique tax accounting firm specializing in tax support for public accounting firms. However, I also provide Canadian and U.S. tax advisory and compliance services to the general public.</p>
    <p>Feel free to contact me if I can be of assistance to you or to your clients.</p>

    <div class="contact">
      <div class="contact-name">Daniel R. Farrow, CGA<br>R. Winslow Farrow Inc.</div>
      <div class="contact-row">
        <svg width="9" height="9" viewBox="0 0 10 10"><rect width="10" height="10" fill="var(--gold)"/><path d="M5 2a2 2 0 0 1 2 2c0 1.5-2 4-2 4S3 5.5 3 4a2 2 0 0 1 2-2z" fill="var(--panel)"/></svg>
        <span>18-410 Harbourview Road<br>Bedford, NS B4A 2K7</span>
      </div>
      <div class="contact-row">
        <svg width="9" height="9" viewBox="0 0 10 10"><rect width="10" height="10" fill="var(--gold)"/><path d="M3 2h1.5l.7 1.8-.9.7a5 5 0 0 0 1.7 1.7l.7-.9L8.5 6v1.5C5 8 2.5 5.5 3 2z" fill="var(--panel)"/></svg>
        <span>(902) 555-0148</span>
      </div>
      <div class="contact-row">
        <svg width="9" height="9" viewBox="0 0 10 10"><rect width="10" height="10" fill="var(--gold)"/><rect x="2" y="3" width="6" height="4" fill="var(--panel)"/><path d="M2 3l3 2.3L8 3" stroke="var(--gold)" stroke-width=".7" fill="none"/></svg>
        <span>daniel@farrowtax.services</span>
      </div>
      <div class="contact-row">
        <svg width="9" height="9" viewBox="0 0 10 10"><rect width="10" height="10" fill="var(--gold)"/><circle cx="5" cy="5" r="2.8" fill="var(--panel)"/></svg>
        <span>www.farrowtax.services</span>
      </div>
    </div>
    <div class="portrait" role="img" aria-label="Portrait photo of Daniel R. Farrow"></div>
  </div>

  <div class="stamp-box">STAMP</div>
  <div class="address-line" style="top:182px"></div>
  <div class="address-line" style="top:224px"></div>
  <div class="address-line" style="top:266px"></div>
  <div class="address-line" style="top:308px"></div>
</section>

</body>
</html>
```